Broschüre für Konzepte rund um Immobilien
Zielgruppe
Wir sind ein junges, dynamisches Team und unterstützen Kunden mit individuellen, abgestimmten Konzepten rund um Ihre Immobilie - daher suchen wir ein hochwertiges Design, unsere Zielgruppe liegt Wert auf was neues, nicht das was jeder hat.
Aufgabenstellung
Die Farben und das Layout sollen von der Homepage übernommen werden www.k7-zelt.de..
Den Text entnehmen Sie der angehängten Datei. Bilder, Anordnungen und sonstiges überlasse ich Ihren kreativen Geist! DIN A5 Querformat - Bilder und Texte müssen in einer sehr hohen Auflösung umsetzbar sein!

```html
<!DOCTYPE html>
<html lang="de">
<head>
<meta charset="utf-8">
<title>K7ZELT Broschüre</title>
<link href="https://fonts.googleapis.com/css2?family=Open+Sans:wght@400;600;700&family=Playfair+Display:wght@400&display=swap" rel="stylesheet">
<style>
  :root {
    --navy: #1d2336;
    --navy-soft: rgba(29, 35, 54, 0.92);
    --paper: #ffffff;
    --stage: #e9e8ec;
    --ink: #2a2a2e;
    --ghost: #d9d8de;
  }
  * { box-sizing: border-box; margin: 0; padding: 0; }
  html, body { width: 1200px; height: 2711px; overflow: hidden; }
  body { background: var(--stage); font-family: "Open Sans", Arial, sans-serif; color: var(--ink); position: relative; }

  .page, .back-cover, .front-cover { position: absolute; overflow: hidden; background: var(--paper); box-shadow: 0 6px 18px rgba(0,0,0,.12); }
  .spread { position: absolute; left: 60px; width: 1080px; height: 380px; box-shadow: 0 6px 18px rgba(0,0,0,.12); overflow: hidden; background: var(--paper); }
  .spread .half { position: absolute; top: 0; width: 540px; height: 380px; overflow: hidden; }
  .spread .half.left { left: 0; }
  .spread .half.right { left: 540px; border-left: 1px solid #e2e2e6; }

  .photo { position: absolute; }
  .band { position: absolute; bottom: 22px; height: 58px; background: var(--navy-soft); color: #fff;
          font-weight: 600; font-size: 14px; letter-spacing: 2px; text-transform: uppercase;
          display: flex; align-items: center; }
  .band.center { justify-content: center; }
  .rule { position: absolute; height: 3px; background: #fff; bottom: 86px; }

  .digit { position: absolute; font-family: "Playfair Display", Georgia, serif; font-size: 300px; line-height: 1; color: var(--ghost); }
  .copy { position: absolute; font-size: 9.5px; line-height: 1.45; text-align: justify; }
  .copy p + p { margin-top: 9px; }
  .copy h2 { font-size: 14px; font-weight: 700; margin: 10px 0 8px; text-align: left; }
  .copy h3 { font-size: 10.5px; font-weight: 700; margin-bottom: 10px; text-align: left; }

  /* covers */
  .front-cover { left: 60px; top: 60px; width: 540px; height: 400px; }
  .front-cover .photo { left: 0; top: 0; width: 540px; height: 250px; background: linear-gradient(135deg, #cfcfca, #8c7f72 50%, #3c3a38); }
  .front-cover .cover-band { position: absolute; left: 0; top: 258px; width: 540px; height: 120px; background: var(--navy); color: #fff; }
  .cover-band .mark-box { position: absolute; left: 20px; top: 18px; width: 70px; height: 70px; border: 1.5px solid #fff; opacity: .7; }
  .cover-band .brand { position: absolute; left: 108px; top: 40px; font-size: 17px; font-weight: 600; letter-spacing: 1px; }
  .cover-band .claim { position: absolute; left: 200px; top: 30px; font-size: 15px; font-weight: 700; letter-spacing: 2.5px; }
  .cover-band .claim-sub { position: absolute; left: 200px; top: 58px; font-size: 10.5px; padding-top: 4px; border-bottom: 1px solid #fff; padding-bottom: 6px; width: 300px; }
  .front-cover .cover-line { position: absolute; left: 0; top: 251px; width: 540px; height: 3px; background: #fff; }

  .back-cover { left: 640px; top: 150px; width: 500px; height: 300px; background: var(--navy); color: #fff; }
  .back-cover svg { position: absolute; inset: 0; }
  .back-cover .brand { position: absolute; left: 40px; top: 80px; font-size: 16px; font-weight: 600; letter-spacing: 1px; }
  .back-cover .contact { position: absolute; left: 200px; top: 78px; font-size: 9.5px; line-height: 1.6; }
</style>
</head>
<body>

<!-- Covers -->
<section class="front-cover">
  <div class="photo" role="img" aria-label="Wohnraum mit Ledersofa und Frau mit Tasse am Fenster"></div>
  <div class="cover-line"></div>
  <div class="cover-band">
    <div class="mark-box"></div>
    <div class="brand">K7ZELT</div>
    <div class="claim">BERATEN • BETREUEN • BEGLEITEN</div>
    <div class="claim-sub">Kompetenz und Know-How im Wohnungsbau</div>
  </div>
</section>

<section class="back-cover">
  <svg width="500" height="300" viewBox="0 0 500 300" aria-hidden="true">
    <path d="M0 30 Q250 60 500 230" stroke="#fff" stroke-width="2" fill="none" opacity=".8"/>
    <path d="M0 150 Q260 150 500 280" stroke="#fff" stroke-width="1" fill="none" opacity=".5"/>
  </svg>
  <div class="brand">K7ZELT</div>
  <div class="contact">K7ZELT – Lena Beispiel<br>Musterweg 12 · 12345 Beispielstadt<br>www.k7-zelt.de</div>
</section>

<!-- Spread 1 -->
<section class="spread" style="top:560px">
  <div class="half left">
    <div class="photo" style="left:0;top:0;width:540px;height:380px;background:linear-gradient(160deg,#c9d6c4,#8fa785 45%,#5b6d7c);" role="img" aria-label="Familie vor dem Eingang ihres Hauses"></div>
    <div class="rule" style="left:0;width:540px"></div>
    <div class="band" style="left:0;width:540px;padding-left:30px">Hand in Hand wird Ihr Hausprojekt optimal geplant</div>
  </div>
  <div class="half right">
    <div class="copy" style="left:30px;top:55px;width:330px">
      <h3 style="font-size:12px">Wir möchten, dass sie glücklich sind.</h3>
      <p>Dass Sie von uns Ihr persönliches Konzept erhalten und in ein Haus ziehen, welches die Grundlage für ein freudvolles und lebenslustiges Leben bietet. Ein Haus, welches gerade im Inneren, Ihnen, Ihrer Persönlichkeit und den Bedürfnissen aller Bewohner entspricht.</p>
      <p>Mit individuellen Gesamtkonzepten ist es K7ZELT ein Bedürfnis, Ihren Lebens(t)raum so auf Ihre Persönlichkeit und Bedürfnisse abzustimmen, dass Ihr persönliches Glück und Freude beim Wohnen gleich mit einziehen.</p>
      <p>Hand in Hand wird durch kurze Kommunikationswege, enge Zusammenarbeit mit den einzelnen Fachplanern und der gemeinsamen Betreuung Ihr Hausprojekt optimal geplant.</p>
    </div>
    <div class="photo" style="right:0;top:0;width:130px;height:380px;background:linear-gradient(180deg,#d8d3c8,#a99a88 60%,#6e6154);" role="img" aria-label="Kind läuft fröhlich durch die Haustür"></div>
    <div class="band" style="left:0;width:540px"></div>
  </div>
</section>

<!-- Spread 2 -->
<section class="spread" style="top:1110px">
  <div class="half left">
    <div class="photo" style="left:0;top:0;width:115px;height:380px;background:linear-gradient(180deg,#e6dde0,#c7b8bf 50%,#9aa0b3);" role="img" aria-label="Hand unterschreibt ein Dokument"></div>
    <div class="digit" style="left:110px;top:10px">1</div>
    <div class="copy" style="left:180px;top:55px;width:330px">
      <p>Die Bemusterung für die Hausbaudetails steht an – unser Berater von K7ZELT trifft sich mit Ihnen zum Gespräch, bei dem Sie sich kennenlernen. Sie berichten wie Sie derzeit leben und Sie erzählen von Ihren Wünschen und vor allem, wie Sie sich Ihr zukünftiges Zuhause vorstellen. Natürlich wird hierbei jeder Raum, sowie Ihre eigenen Stilwünsche unter die Lupe genommen.</p>
      <h2>Ihr zukünftiges Haus in guten Händen.</h2>
      <p>Im Anschluss des Gespräches werden sämtliche Ideen und Konzepte an die jeweiligen Partnerfirmen übergeben. Jetzt sind alle entscheidenden Details in guten Händen, um von nun an die optimale Planung für Sie angehen zu können.</p>
    </div>
    <div class="band center" style="left:0;width:540px;padding-left:115px">Das Vorgespräch</div>
  </div>
  <div class="half right">
    <div class="digit" style="left:210px;top:10px">2</div>
    <div class="copy" style="left:30px;top:75px;width:230px">
      <h3>Egal ob Fliesen, Parkett oder Teppichboden -</h3>
      <p>ein Fußboden bildet das bestimmende „Fundament“ für das Raumgefühl in Ihren Räumen. Fußböden sollten so gewählt sein, dass man sich lange darüber freuen kann und sich anschließend nicht ärgert.</p>
      <p>Aber es ist erneut wichtig, dass die Auswahl zur Raumwirkung und den Möbelvorstellungen passt – hier ist Erfahrung gefragt!</p>
    </div>
    <div class="photo" style="right:0;top:0;width:195px;height:380px;background:linear-gradient(170deg,#eeeae4,#bca48a 55%,#8b6c4c);" role="img" aria-label="Offener Wohnraum mit Esstisch und Holzboden"></div>
    <div class="band" style="left:0;width:540px;padding-left:30px">Ihr persönliches Fussboden Konzept</div>
  </div>
</section>

<!-- Spread 3 -->
<section class="spread" style="top:1660px">
  <div class="half left">
    <div class="photo" style="left:0;top:0;width:230px;height:380px;background:linear-gradient(180deg,#d9d6d1,#9d9488 55%,#4e4a46);" role="img" aria-label="Badezimmer mit freistehender Wanne"></div>
    <div class="digit" style="left:180px;top:10px">3</div>
    <div class="copy" style="left:305px;top:75px;width:200px">
      <p>Wer sein Bad nach eigenen Wünschen gestalten möchte, hat heute die Qual der Wahl. Entscheiden Sie sich für die Wellness-Oase oder doch lieber das funktionale Bad mit bedacht auf das Alter?</p>
      <h2 style="font-size:12px">Warum nicht beides?</h2>
      <p>Wir nennen es das Bad zum Wohlfühlen, ausgerichtet auf Ihre Wünsche und Bedürfnisse.</p>
    </div>
    <div class="band center" style="left:0;width:540px;padding-left:10px">Ihr persönliches Bad Konzept</div>
  </div>
  <div class="half right">
    <div class="copy" style="left:30px;top:80px;width:150px">
      <p>Sie treffen sich nach ca. 4 Wochen wieder. Gemeinsam mit unserem Berater gehen Sie nun zu unseren Partnerfirmen das gesamte Gestaltungskonzept durch und stimmen Details nochmals ab.</p>
      <p>Inhaltliche &amp; organisatorische Fragen für die Umsetzung werden geklärt.</p>
    </div>
    <div class="photo" style="right:0;top:0;width:310px;height:380px;background:linear-gradient(150deg,#f3e8dc,#d9c3ad 45%,#9fa6b2);" role="img" aria-label="Händedruck über Planungsunterlagen"></div>
    <div class="digit" style="left:175px;top:10px;opacity:.8">4</div>
    <div class="band" style="left:0;width:540px;padding-left:80px">Ihre Planung ist fertig</div>
  </div>
</section>

<!-- Spread 4 -->
<section class="spread" style="top:2210px">
  <div class="photo" style="left:0;top:0;width:690px;height:380px;background:radial-gradient(ellipse at 30% 20%,#fbe8c6,#d99a5c 40%,#6e5a4e 80%);" role="img" aria-label="Zwei Hände fügen Puzzleteile im Gegenlicht zusammen"></div>
  <div class="rule" style="left:0;width:690px"></div>
  <div class="band" style="left:0;width:690px"></div>
  <div class="half right" style="background:transparent;border:none">
    <div class="digit" style="left:150px;top:10px">5</div>
    <div class="copy" style="left:230px;top:85px;width:280px;text-align:left">
      <p>Nun haben Sie alle Möglichkeiten, Ihre individuelle Raumgestaltung umzusetzen.</p>
      <h3 style="margin-top:10px">K7ZELT unterstützt Sie weiterhin gerne im Bereich Möbel- &amp; Küchenkonzepte.</h3>
      <p>Wann und wie Sie Empfehlungen oder das gesamte Konzept verwirklichen, entscheiden Sie selbst…</p>
    </div>
    <div class="band center" style="left:150px;width:390px">In Verbindung bleiben</div>
  </div>
</section>

</body>
</html>
```